Auction Gallery Consignment info brochure

We need to create a 8.5" x 5.5" single fold brochure that will visually explain the details of the consignment process of our business Brinkmoor Bidhouse and be attractive to new customers looking to consign items to us. We have included a word doc that outlines the process and terms as well as some photos of items we have sold and the prices realized. other info to add in the brochure about our company can be found on our website www.brinkmoorbidhouse.example
that is also where you will find our logo, which will have to be copied over and possibly remade as we have lost the original high res files of it. feel free to use standard auction graphics such as gavels or similar things found online, we want it to be a little fancy and refined looking, not like we are a farm equip auction but portraying that we sell valuable estate merchandise such as valuable antiques and mid-century design. call us with any questions concerning the brochure creation 555-418-7062
the photos attached correspond with the list of prices realized in the word document

Target Market(s)

40-70year olds looking to sell unique items at live auction

Industry/Entity Type

Business

Font styles to use
Sans Serif

Requirements
Must have
• a good cover with our logo "brinkmoor bidhouse" and maybe an auction graphic, the inside having two pages one detailing the process and the other showing the prices realized and photos of those items, the back cover can also have auction related graphics and our company contact info
Should not have
• Photos of staff members

```html
<!DOCTYPE html>
<html lang="en">
<head>
<meta charset="utf-8">
<title>Brinkmoor Bidhouse – Consignment Brochure</title>
<link rel="stylesheet" href="https://fonts.googleapis.com/css2?family=Source+Sans+3:ital,wght@0,400;0,600;0,700;1,400&display=swap">
<style>
:root{
  --stage:#2a2a2a;
  --paper:#ffffff;
  --green:#7ba33a;
  --green-dark:#5f8a22;
  --green-soft:#e5edd3;
  --ink:#3a3a3a;
  --muted:#6b6b6b;
  --cream:#f6f0e4;
  --cream-edge:#ece2cf;
  --red:#b5261e;
  --black:#0c0c0c;
  --grey-hi:#fafafa;
  --grey-lo:#cfcfcf;
}
*{box-sizing:border-box;margin:0;padding:0}
html,body{width:1121px;height:1200px;overflow:hidden}
body{background:var(--stage);font-family:"Source Sans 3",Arial,sans-serif;color:var(--ink);position:relative}

/* ---------- Outer spread ---------- */
.outer{position:absolute;left:125px;top:19px;width:856px;height:551px;background:var(--paper);overflow:hidden}
.outer-back{position:absolute;left:20px;top:13px;width:415px;height:525px;background:var(--green)}
.outer-front{position:absolute;left:435px;top:13px;width:401px;height:525px;background:linear-gradient(135deg,var(--grey-hi) 30%,var(--grey-lo))}
.hero-photo{position:absolute;left:361px;top:-10px;width:468px;height:468px;border-radius:50%;
  background:radial-gradient(circle at 42% 40%,#6b5a33 0,#3b3222 18%,var(--black) 52%);border:6px solid var(--paper)}
.gavel-photo{position:absolute;left:641px;top:271px;width:168px;height:168px;border-radius:50%;
  background:radial-gradient(circle at 45% 50%,#7a4a22 0,#b98a5c 30%,#f3f1ee 62%);border:5px solid var(--paper);box-shadow:0 2px 6px rgba(0,0,0,.25)}
.contact{position:absolute;left:34px;top:448px;color:#fff;font-size:15px;line-height:1.3}
.contact strong{font-weight:700;font-size:16px}
.brand{position:absolute;right:38px;top:474px;display:flex;align-items:center;gap:7px}
.brand-mark{width:12px;height:12px;background:var(--muted)}
.brand-name{font-size:23px;font-weight:400;color:var(--muted);letter-spacing:.01em;white-space:nowrap}

/* ---------- Inside spread ---------- */
.inside{position:absolute;left:121px;top:603px;width:863px;height:564px;
  background:radial-gradient(ellipse at center,var(--cream) 55%,var(--cream-edge));overflow:hidden}
.panel-left{position:absolute;left:0;top:0;width:440px;height:100%}
.panel-right{position:absolute;left:440px;top:0;width:423px;height:100%}

.tab{position:absolute;left:0;top:28px;height:28px;width:168px;background:var(--green);color:#fff;white-space:nowrap;
  font-weight:700;font-size:16px;letter-spacing:.04em;padding:3px 0 0 30px;clip-path:polygon(0 0,100% 0,90% 100%,0 100%)}
.intro{position:absolute;left:30px;top:68px;width:390px;font-style:italic;font-size:13px;line-height:1.35;color:var(--muted)}
.process-title{position:absolute;left:30px;top:135px;font-size:11.5px;font-weight:700;color:var(--ink)}
.process{position:absolute;top:153px;width:188px;font-size:10px;line-height:1.3;color:var(--ink);list-style:none}
.process-a{left:30px}
.process-b{left:236px}
.process li{position:relative;padding-left:9px;margin-bottom:8px}
.process li::before{content:"";position:absolute;left:0;top:5px;width:4px;height:4px;background:var(--ink)}
.services{position:absolute;left:18px;top:340px;width:412px;height:160px;background:var(--green-soft);border-left:4px solid var(--green);padding:10px 14px}
.services h2{font-size:16px;font-weight:700;color:var(--green-dark);letter-spacing:.03em;margin-bottom:4px}
.services p{font-size:10.5px;line-height:1.3;color:var(--ink);margin-bottom:8px}
.services .cats{color:var(--green-dark)}
.closing{position:absolute;left:30px;top:512px;width:395px;font-size:10.5px;line-height:1.3;color:var(--muted)}

.results-title{position:absolute;left:10px;top:28px;padding-left:10px;border-left:3px solid var(--red);
  font-size:15px;font-weight:700;color:var(--ink);letter-spacing:.02em;line-height:1.15}
.lot{position:absolute;width:195px;height:112px}
.lot-photo{position:absolute;left:0;top:0;width:82px;height:96px;border-radius:6px}
.lot-info{position:absolute;left:90px;top:0;width:102px}
.lot-name{font-size:10.5px;font-weight:600;text-transform:uppercase;line-height:1.15;color:var(--ink)}
.lot-est{font-size:10px;color:var(--muted);line-height:1.2;margin-top:6px}
.sold{position:absolute;left:90px;top:78px;height:22px;width:102px;background:var(--red);color:#fff;font-size:10px;padding:4px 0 0 7px;white-space:nowrap;
  clip-path:polygon(0 0,100% 0,92% 50%,100% 100%,0 100%)}
.sold b{font-size:13px;font-weight:700}
.lot-wide .lot-photo{width:150px;height:76px}
.lot-wide .lot-info{left:160px;width:200px}
.lot-wide .sold{left:160px;top:50px;width:120px}
.ph-light{background:linear-gradient(160deg,#fbf8f2,#ddd6c8)}
.ph-dark{background:linear-gradient(160deg,#3a2e20,#0f0d0a)}
.ph-warm{background:linear-gradient(160deg,#eadfcd,#a98b63)}
</style>
</head>
<body>

<section class="outer" aria-label="Outer spread">
  <div class="outer-back"></div>
  <div class="outer-front"></div>
  <div class="hero-photo" role="img" aria-label="Photograph of a vintage gold wristwatch on a black leather strap with its reflection"></div>
  <div class="gavel-photo" role="img" aria-label="Photograph of a wooden auction gavel"></div>
  <div class="contact">
    Brinkmoor Bidhouse location and contact info:<br>
    42 Alder Quay, Brinkmoor, ST 00000<br>
    <strong>555-418-7062</strong> &nbsp;|&nbsp; www.brinkmoorbidhouse.example
  </div>
  <div class="brand"><span class="brand-mark"></span><span class="brand-name">Brinkmoor Bidhouse</span></div>
</section>

<section class="inside" aria-label="Inside spread">
  <div class="panel-left">
    <div class="tab">WHO WE ARE:</div>
    <p class="intro">At Brinkmoor Bidhouse we strive to provide outstanding service to our clients. We appraise, market, and sell your items for the best market value they can achieve at live auction.</p>
    <h3 class="process-title">CONSIGNMENT PROCESS:</h3>
    <ul class="process process-a">
      <li>Email us photos to: info@brinkmoorbidhouse.example or call us at 555-418-7062 to describe what you would like to sell or set up an appointment for one of our evaluators to come see what you have</li>
      <li>Come into our Brinkmoor gallery on a Friday 10am-5pm for “Find out Friday” and get a no obligation evaluation of your items</li>
    </ul>
    <ul class="process process-b">
      <li>Once we have agreed on the potential consignments and the value at auction, we can determine a commission rate to sell your items, you fill out a contract, and the items are listed in our next monthly auction.</li>
      <li>We handle all the transport, insurance, advertising, and collecting of payment.</li>
      <li>45 days after the auction a check is issued for the proceeds of the sale.</li>
    </ul>
    <div class="services">
      <h2>SERVICES WE PROVIDE:</h2>
      <p>We handle single or multiple consignments, estate cleanouts, and liquidations for items in the following categories:</p>
      <p class="cats">17th Century to Contemporary Paintings • Old Masters • Furniture • Antiques Sculpture and Ceramics • Chinese Art, Ceramics, Jade, Sculpture, and Jewelry 20th Century Design and Mid-Century Modern • American Fine Art Indian Folk Art and Ceramics • Impressionist paintings • Modern, and Local Art Books &amp; Manuscripts • Clocks and Barometers • Judaica • Jewelry • Musical Instruments Prints • Rugs and Carpets • Silver • Automobiles • Industrial design</p>
    </div>
    <p class="closing">With the knowledge to handle a wide range of items, our specialists are here to help you and your consignments realize their maximum potential of the sale.</p>
  </div>

  <div class="panel-right">
    <h2 class="results-title">WE ACHIEVE SURPRISING RESULTS<br>FOR OUR CLIENTS, FOR EXAMPLE:</h2>

    <div class="lot" style="left:18px;top:80px">
      <div class="lot-photo ph-light" role="img" aria-label="Photograph of a brass multi-arm chandelier"></div>
      <div class="lot-info"><div class="lot-name">Aarno Vellinen Chandelier</div><div class="lot-est">Estimated<br>30,000 — 50,000</div></div>
      <div class="sold">SOLD for <b>$70,000</b></div>
    </div>
    <div class="lot" style="left:215px;top:80px">
      <div class="lot-photo ph-light" role="img" aria-label="Photograph of a ceramic owl vase"></div>
      <div class="lot-info"><div class="lot-name">Teodor Vasquel Wood Owl Vase</div><div class="lot-est">Estimated<br>10,000 — 15,000</div></div>
      <div class="sold">SOLD for <b>$16,000</b></div>
    </div>

    <div class="lot" style="left:18px;top:198px">
      <div class="lot-photo ph-dark" role="img" aria-label="Photograph of a gold wristwatch on a black strap"></div>
      <div class="lot-info"><div class="lot-name">Halvorsen Frères Mens Meridian 18K Gold Watch</div><div class="lot-est">Estimated<br>4,000 — 6,000</div></div>
      <div class="sold">SOLD for <b>$16,000</b></div>
    </div>
    <div class="lot" style="left:215px;top:198px">
      <div class="lot-photo ph-light" role="img" aria-label="Photograph of an ornate silver crown"></div>
      <div class="lot-info"><div class="lot-name">German or Silesian Torah Crown</div><div class="lot-est">Estimated<br>4,000 — 6,000</div></div>
      <div class="sold">SOLD for <b>$20,000</b></div>
    </div>

    <div class="lot" style="left:18px;top:316px">
      <div class="lot-photo ph-warm" role="img" aria-label="Photograph of a carved reliquary guardian figure"></div>
      <div class="lot-info"><div class="lot-name">African Kota Reliquary Guardian Figure</div><div class="lot-est">Estimated<br>10,000 — 15,000</div></div>
      <div class="sold">SOLD for <b>$46,000</b></div>
    </div>
    <div class="lot" style="left:215px;top:316px">
      <div class="lot-photo ph-warm" role="img" aria-label="Photograph of a pen and ink drawing"></div>
      <div class="lot-info"><div class="lot-name">Harlan Whitcombe Pen &amp; Ink Drawing</div><div class="lot-est">Estimated<br>5,000 — 7,000</div></div>
      <div class="sold">SOLD for <b>$18,000</b></div>
    </div>

    <div class="lot lot-wide" style="left:18px;top:452px;width:380px">
      <div class="lot-photo ph-dark" role="img" aria-label="Photograph of a carved pale jade figure"></div>
      <div class="lot-info"><div class="lot-name">Qing Dynasty Carved Jade Figure</div><div class="lot-est">Estimated 1,200 — 1,600</div></div>
      <div class="sold">SOLD for <b>$10,000</b></div>
    </div>
  </div>
</section>

</body>
</html>
```